Bright Fern Custom Homes business card. Double sided. Modern. professional

Bright Fern Custom Homes
contemporary modern design with our logo /
Double sided with all our contact information
Use same Green colors as in our Logo. Contemporary logo that grabs your attention. Visually pleasing and balanced. Easy to read, and Vibrant. Would love an option for rounded edges. Embossed logo would be amazing.
Contact Information for Business Card
Dana Welk Owner / General Contractor Bright Fern Custom Homes p: 704.552.1830 m: 912.648.2071 e: brightferncustomhomes@mailbox.example w: www.brightferncustomhomes.example 218 Pryor Meadow Lane Alder Glen, NC 29041

```html
<!DOCTYPE html>
<html lang="en">
<head>
<meta charset="utf-8">
<title>Bright Fern Custom Homes — Business Card</title>
<link href="https://fonts.googleapis.com/css2?family=Cinzel:wght@400&family=Arimo:wght@400&display=swap" rel="stylesheet">
<style>
  :root {
    --page-bg: #e3e4e6;
    --card-white: #ffffff;
    --green-text: #5b7229;
    --green-name: #76923c;
    --green-dark: #5b6f31;
    --green-light: #76923c;
    --green-emboss: #86a34c;
  }
  * { margin: 0; padding: 0; box-sizing: border-box; }
  html, body { width: 1200px; height: 1166px; overflow: hidden; }
  body { background: var(--page-bg); position: relative; font-family: "Arimo", Arial, sans-serif; }

  .card {
    position: absolute; top: 471px; width: 412px; height: 235px;
    border-radius: 18px; overflow: hidden;
  }
  .card--front { left: 153px; background: var(--card-white); color: var(--green-text); }
  .card--back { left: 611px; background: var(--green-dark); }

  .brand { position: absolute; font-family: "Cinzel", serif; font-weight: 400; text-align: center; }
  .brand__name { display: block; line-height: 1; letter-spacing: 0.5px; }
  .brand__sub { display: block; }

  .front-brand { left: 14px; width: 168px; top: 110px; color: var(--green-text); }
  .front-brand .brand__name { font-size: 20px; }
  .front-brand .brand__sub { font-size: 6px; letter-spacing: 5px; margin-top: 2px; }
  .brand-mark { position: absolute; left: 76px; top: 45px; width: 44px; height: 44px; background: var(--green-light); }

  .rule { position: absolute; height: 1px; background: var(--green-text); }
  .rule--left { left: 14px; width: 168px; top: 147px; }
  .rule--right { left: 185px; width: 210px; top: 150px; }

  .person { position: absolute; right: 17px; top: 104px; text-align: right; }
  .person__name { font-family: "Cinzel", serif; font-size: 17px; letter-spacing: 0.5px; color: var(--green-name); line-height: 1.1; }
  .person__title { font-size: 11px; line-height: 1.3; }

  .contacts { position: absolute; right: 14px; top: 165px; list-style: none; font-size: 11px; line-height: 13.5px; text-align: right; }
  .contacts li { display: flex; justify-content: flex-end; align-items: center; gap: 6px; }
  .contacts svg { width: 8px; height: 8px; flex: none; }

  .address { position: absolute; left: 15px; top: 193px; font-size: 11px; line-height: 13.5px; font-style: normal; }

  .back-decor { position: absolute; inset: 0; width: 100%; height: 100%; }
  .back-brand { left: 22px; width: 229px; top: 185px; color: var(--green-emboss); }
  .back-brand .brand__name { font-size: 25px; }
  .back-brand .brand__sub { font-size: 7px; letter-spacing: 6px; margin-top: 4px; }
</style>
</head>
<body>

<section class="card card--front" aria-label="Business card front">
  <div class="brand-mark" aria-hidden="true"></div>
  <div class="brand front-brand">
    <span class="brand__name">BRIGHT FERN</span>
    <span class="brand__sub">CUSTOM HOMES</span>
  </div>
  <div class="rule rule--left"></div>

  <div class="person">
    <p class="person__name">DANA WELK</p>
    <p class="person__title">Owner / General Contractor</p>
  </div>
  <div class="rule rule--right"></div>

  <ul class="contacts">
    <li>704.552.1830
      <svg viewBox="0 0 10 10"><path d="M2 1l2 2-1 1.2c.6 1.2 1.5 2.1 2.8 2.8L7 6l2 2-1.3 1.3C4.5 9 1 5.5.7 2.3z" fill="var(--green-text)"/></svg></li>
    <li>912.648.2071
      <svg viewBox="0 0 10 10"><rect x="2.5" y="0.5" width="5" height="9" rx="1" fill="none" stroke="var(--green-text)"/></svg></li>
    <li>brightferncustomhomes@mailbox.example
      <svg viewBox="0 0 10 10"><rect x="0.5" y="2" width="9" height="6" fill="var(--green-text)"/><path d="M0.5 2l4.5 3.5L9.5 2" fill="none" stroke="#fff" stroke-width=".8"/></svg></li>
    <li>www.brightferncustomhomes.example
      <svg viewBox="0 0 10 10"><circle cx="5" cy="5" r="4.5" fill="var(--green-text)"/><path d="M.5 5h9M5 .5v9" stroke="#fff" stroke-width=".6"/></svg></li>
  </ul>

  <address class="address">
    218 Pryor Meadow Lane<br>
    Alder Glen, NC 29041
  </address>
</section>

<section class="card card--back" aria-label="Business card back">
  <svg class="back-decor" viewBox="0 0 412 235" preserveAspectRatio="none" role="img" aria-label="Large lighter green leaf shape sweeping across the right side of the card">
    <defs>
      <linearGradient id="leafTone" x1="0" y1="1" x2="1" y2="0">
        <stop offset="0.45" stop-color="#5b6f31"/>
        <stop offset="0.62" stop-color="#76923c"/>
      </linearGradient>
    </defs>
    <rect width="412" height="235" fill="url(#leafTone)"/>
  </svg>
  <div class="brand back-brand">
    <span class="brand__name">BRIGHT FERN</span>
    <span class="brand__sub">CUSTOM HOMES</span>
  </div>
</section>

</body>
</html>
```